Pelvin Advisory Business Card Design

Business card for business consulting company, using attached logo. We do financial and strategic consulting, and want a clean, professional image with a bit of fun. Our logo is a flat whale tail, which symbolizes the Orca whale, a highly collaborative, group based animal that is very successful in navigating the ocean, protecting the herd, and hunting. We like the logo that is blue and gray on white one one side, but would be open to a blue card with white lettering on the other side... or whatever you'd suggest
Updates
Hi all - I have had the logo modified to take the shadowing off the tail. I will post it on the brief... under a file name called updated logo. thank you Added Saturday, April 25, 2015
Target Market(s)
Small to medium sized businesses ($10M to $500M in revenue per year), financial and sales executives, general managers, attorneys and CPAs
Industry/Entity Type
Financial
Contact Information for Business Card
Want company name, contact info - name, title, telephone, email, website, linkedin, twitter and Facebook. No physical address yet.
Requirements
Must have
- contemporary design, bold, strong, confident but with a bit of fun. prominently feature the logo and the whale tail icon
Nice to have
- unique touches that would differentiate us from a regular card... for example, logo and writing all on front on white background, but on back - logo in white on a blue background
- open to idea of different shapes of card than standard... but not sure

```html
<!DOCTYPE html>
<html lang="en">
<head>
<meta charset="utf-8">
<title>Pelvin Advisory Business Card</title>
<link href="https://fonts.googleapis.com/css2?family=Open+Sans:wght@400;600&display=swap" rel="stylesheet">
<style>
  :root {
    --page: #f0f1f0;
    --navy: #003566;
    --white: #ffffff;
    --grey: #a7a9ac;
  }
  * { margin: 0; padding: 0; box-sizing: border-box; }
  html, body { width: 1200px; height: 960px; overflow: hidden; }
  body {
    background: var(--page);
    font-family: "Open Sans", Arial, sans-serif;
    position: relative;
  }
  .card { position: absolute; left: 316px; width: 568px; height: 318px; }
  .card-front { top: 142px; background: var(--white); }
  .card-back { top: 500px; background: var(--navy); }

  .wordmark { position: absolute; display: flex; align-items: center; }
  .wordmark .mark { border-radius: 8px; flex: none; }
  .wordmark .name {
    font-weight: 600; letter-spacing: -1px; white-space: nowrap; line-height: 1;
  }
  .wordmark .tagline {
    position: absolute; right: 0; font-size: 13px; line-height: 1; white-space: nowrap;
  }

  .front-logo { left: 58px; top: 66px; }
  .front-logo .mark { width: 65px; height: 65px; background: var(--navy); }
  .front-logo .name { margin-left: 12px; font-size: 44px; color: var(--navy); }
  .front-logo .tagline { bottom: -16px; color: var(--navy); }

  .contact-band {
    position: absolute; left: 0; bottom: 0; width: 100%; height: 145px;
    background: var(--navy); color: var(--white);
  }
  .person { position: absolute; left: 71px; top: 22px; }
  .person .full-name { font-size: 15px; font-weight: 400; line-height: 1.2; }
  .person .job-title { font-size: 16px; line-height: 1.4; }
  .social { position: absolute; left: 59px; top: 86px; display: flex; gap: 10px; }
  .social span {
    width: 26px; height: 26px; border-radius: 50%;
    background: #0b2c52; box-shadow: 2px 2px 0 rgba(0,0,0,0.25);
  }
  .contact-list {
    position: absolute; right: 28px; top: 23px; list-style: none;
  }
  .contact-list li {
    display: flex; align-items: center; justify-content: flex-end;
    height: 24.5px; font-size: 12.5px; font-weight: 600;
  }
  .contact-list svg { margin-left: 9px; width: 20px; height: 20px; }

  .back-logo { left: 72px; top: 122px; }
  .back-logo .mark { width: 73px; height: 73px; background: var(--white); }
  .back-logo .name { margin-left: 9px; font-size: 48px; color: var(--white); }
  .back-logo .tagline { bottom: -16px; color: var(--white); font-size: 14px; }
</style>
</head>
<body>
  <section class="card card-front">
    <div class="wordmark front-logo">
      <span class="mark"></span>
      <span class="name">Pelvin Advisory</span>
      <span class="tagline">business consulting</span>
    </div>
    <div class="contact-band">
      <div class="person">
        <p class="full-name">Name</p>
        <p class="job-title">title</p>
      </div>
      <div class="social" aria-label="social profiles">
        <span></span><span></span><span></span>
      </div>
      <ul class="contact-list">
        <li>telephone
          <svg viewBox="0 0 20 20"><circle cx="10" cy="10" r="10" fill="#fff"/><path d="M6.5 5.5l2 -0.5 1 2.5-1.2 1c.6 1.3 1.5 2.2 2.7 2.8l1-1.2 2.5 1-.5 2c-4 .3-7.7-3.6-7.5-7.6z" fill="#003566"/></svg></li>
        <li>fax
          <svg viewBox="0 0 20 20"><circle cx="10" cy="10" r="10" fill="#fff"/><rect x="5.5" y="7.5" width="9" height="6" rx="1" fill="none" stroke="#003566" stroke-width="1.4"/><rect x="7.5" y="5" width="5" height="3" fill="#003566"/></svg></li>
        <li>email
          <svg viewBox="0 0 20 20"><circle cx="10" cy="10" r="10" fill="#fff"/><rect x="5" y="6.5" width="10" height="7" rx="1" fill="none" stroke="#003566" stroke-width="1.4"/><path d="M5.5 7l4.5 3.5 4.5-3.5" fill="none" stroke="#003566" stroke-width="1.2"/></svg></li>
        <li>website
          <svg viewBox="0 0 20 20"><circle cx="10" cy="10" r="10" fill="#fff"/><circle cx="10" cy="10" r="5" fill="none" stroke="#003566" stroke-width="1.4"/><path d="M5 10h10M10 5c-2.5 3-2.5 7 0 10M10 5c2.5 3 2.5 7 0 10" fill="none" stroke="#003566" stroke-width="1"/></svg></li>
      </ul>
    </div>
  </section>

  <section class="card card-back">
    <div class="wordmark back-logo">
      <span class="mark"></span>
      <span class="name">Pelvin Advisory</span>
      <span class="tagline">business consulting</span>
    </div>
  </section>
</body>
</html>
```